Sci Fi/ Secret Agent Author needs website design!

My name is Talia Brook and I am an author. I require a site that can provide information about myself and my books and other works.

I would like it to have a Home, blog function, (about the) books/series section so people can visit another section and read about each individual book that's going to be released. A resources page, a Store, social media links and ability to load/embed videos from clipvana and other.

I write mild scifi/thriller/conspiracy/secret government type novels. -At the moment-. The series follows a strong female lead that is an agent with a secret organisation in a classified military installation.

The theme would be professional yet possibly show this element.

Target Market(s)

/military fiction/thriller/fantasy/Sci fi/ femme-fatal, readers. Mostly females, age 18-60
Novel readers

Number of Pages Required

5+ page

Requirements
Must have
• Would like designers to follow brief. :)
• My budget includes all the pages I will need;
• eg home, blog, resources, store, ability to pay with coinlark and Credit Cards
• , ability to have trailers from clipvana etc. Must have links to the social media mentioned in the brief.
Nice to have
• use of the colours I have suggested. electric/indigo purple, fuschia highlights , dark greys
• as I will possibly base branding for social media ETC on the look of your website design and colour scheme.
• Ability for trailer on front page??
Should not have
• Should not be too cluttered. (But I am open to all ideas)

```html
<!DOCTYPE html>
<html lang="en">
<head>
<meta charset="utf-8">
<title>Talia Brook — Author</title>
<link href="https://fonts.googleapis.com/css2?family=Open+Sans:wght@400;600;700;800&display=swap" rel="stylesheet">
<style>
:root{
  --indigo:#2d1270;
  --indigo-dark:#241058;
  --ink:#111111;
  --grey-band:#d9dcdd;
  --muted:#6b6b6b;
  --white:#ffffff;
  --social-a:#3b5998;
  --social-b:#1da1f2;
  --social-c:#4e7fa8;
  --social-d:#c4302b;
}
*{box-sizing:border-box;margin:0;padding:0}
html,body{width:1200px;height:2871px;overflow:hidden}
body{font-family:"Open Sans",Arial,sans-serif;color:var(--ink);background:var(--white);position:relative}

/* Navigation */
.site-nav{position:absolute;left:0;top:0;width:1200px;height:67px;background:var(--white)}
.brand{position:absolute;left:80px;top:19px;font-size:21px;font-weight:800;letter-spacing:.3px}
.menu{position:absolute;left:340px;top:23px;display:flex;gap:26px;font-size:15px;font-weight:700;color:var(--indigo)}
.cart{position:absolute;left:1043px;top:22px;font-size:15px;font-weight:700;display:flex;align-items:center;gap:8px}
.cart-count{display:inline-block;background:var(--ink);color:var(--white);font-size:10px;border-radius:50%;width:16px;height:16px;line-height:16px;text-align:center}

/* Hero */
.hero{position:absolute;left:8px;top:67px;width:1184px;height:565px;background:linear-gradient(135deg,#8e98a0 0%,#5d6b78 45%,#3c4a58 100%)}
.hero-title{position:absolute;left:0;width:1200px;top:255px;text-align:center;font-size:42px;font-weight:800;letter-spacing:.5px}
.hero-title .dot{color:var(--indigo)}
.social-row{position:absolute;top:375px;left:0;width:1200px;display:flex;justify-content:center;gap:18px}
.social{display:flex;align-items:center;gap:6px;font-size:13px;font-weight:700;color:var(--white);white-space:nowrap}
.social .disc{width:54px;height:54px;border-radius:50%;flex:none}

/* Section headings */
.section-title{position:absolute;text-align:center;font-size:42px;font-weight:700;color:var(--indigo)}
.rule{position:absolute;height:2px;width:220px;background:#555}

/* Books */
.books{position:absolute;left:0;top:632px;width:1200px;height:587px;background:var(--grey-band)}
.book{position:absolute;top:153px;width:150px;text-align:center}
.cover{width:150px;height:229px;border:3px solid var(--white)}
.book-title{margin-top:14px;font-size:19px;font-weight:600}
.book-author{font-size:15px;color:var(--muted);margin-top:2px}
.btn{position:absolute;background:var(--indigo);color:var(--white);font-weight:700;font-size:20px;display:flex;align-items:center;justify-content:center}

/* About */
.portrait{position:absolute;left:79px;top:1315px;width:398px;height:398px;border-radius:50%;background:radial-gradient(circle at 50% 40%,#b98c6a 0%,#8a6548 55%,#cfc8bd 100%)}
.about-copy{position:absolute;left:536px;width:596px;font-size:15px;line-height:1.28}

/* Video */
.video{position:absolute;left:8px;top:1809px;width:1184px;height:421px;background:linear-gradient(90deg,#3a3a3a,#4a4a4a 50%,#2e2e2e)}
.play{position:absolute;left:547px;top:1939px}
.video-caption{position:absolute;left:0;width:1200px;top:2072px;text-align:center;color:var(--white);font-size:16px;letter-spacing:2px}

/* Blog */
.post{position:absolute;top:2394px;width:328px}
.post-image{height:192px;background:linear-gradient(160deg,#e9dcc9,#c9a27a 60%,#dfe6ee)}
.post-body{height:165px;background:var(--indigo);color:var(--white);padding:14px 18px 0}
.post-title{font-size:30px;font-weight:600;text-align:center}
.post-text{font-size:14.5px;font-weight:700;line-height:1.2;margin-top:10px}

/* Footer */
.footer{position:absolute;left:0;top:2806px;width:1200px;height:65px;background:var(--grey-band);overflow:hidden}
.copyright{position:absolute;left:480px;top:22px;font-size:14px;color:var(--indigo-dark)}
.footer-social{position:absolute;right:60px;top:20px;display:flex;gap:10px}
.footer-social .social{font-size:10px;color:var(--indigo);gap:4px}
.footer-social .disc{width:24px;height:24px}
</style>
</head>
<body>

<header class="site-nav">
  <div class="brand">TALIA BROOK</div>
  <nav class="menu"><span>HOME</span><span>ABOUT TALIA BROOK</span><span>BOOKS</span><span>BLOG</span><span>RESOURCES</span><span>CONTACT</span></nav>
  <div class="cart">
    <svg width="14" height="15" viewBox="0 0 14 15"><path d="M4 5V3.5a3 3 0 0 1 6 0V5" fill="none" stroke="#111" stroke-width="1.6"/><rect x="1" y="5" width="12" height="10" fill="#111"/></svg>
    CART <span class="cart-count">0</span>
  </div>
</header>

<section class="hero" role="img" aria-label="Collage of conspiracy newspaper clippings, maps and symbols connected by lines"></section>
<h1 class="hero-title">SCI-FI <span class="dot">•</span> THRILLER <span class="dot">•</span> CONSPIRACY</h1>
<div class="social-row">
  <div class="social"><span class="disc" style="background:var(--social-a)"></span>friendloop</div>
  <div class="social"><span class="disc" style="background:var(--social-b)"></span>chirpwave</div>
  <div class="social"><span class="disc" style="background:var(--social-c)"></span>snapmosaic</div>
  <div class="social"><span class="disc" style="background:var(--social-d)"></span>clipvana</div>
</div>

<section class="books">
  <h2 class="section-title" style="left:0;width:1200px;top:38px">DISCOVER YOUR NEXT BOOK</h2>
  <div class="rule" style="left:490px;top:108px"></div>
  <div class="book" style="left:88px"><div class="cover" role="img" aria-label="Book cover: The Forest" style="background:linear-gradient(180deg,#1a9a6c 0 45%,#7a4a2a 45%,#3d2a1a)"></div><div class="book-title">The Forest</div><div class="book-author">Owen Hale</div></div>
  <div class="book" style="left:264px"><div class="cover" role="img" aria-label="Book cover: The Son" style="background:linear-gradient(180deg,#c8a88c,#8c6a52)"></div><div class="book-title">The Forest</div><div class="book-author">Owen Hale</div></div>
  <div class="book" style="left:440px"><div class="cover" role="img" aria-label="Book cover: Life in the Garden" style="background:linear-gradient(180deg,#3a3a3a 0 70%,#e0392b 70%)"></div><div class="book-title">The Forest</div><div class="book-author">Owen Hale</div></div>
  <div class="book" style="left:616px"><div class="cover" role="img" aria-label="Book cover: The Forest" style="background:linear-gradient(180deg,#1a9a6c 0 45%,#7a4a2a 45%,#3d2a1a)"></div><div class="book-title">The Forest</div><div class="book-author">Owen Hale</div></div>
  <div class="book" style="left:792px"><div class="cover" role="img" aria-label="Book cover: The Son" style="background:linear-gradient(180deg,#c8a88c,#8c6a52)"></div><div class="book-title">The Forest</div><div class="book-author">Owen Hale</div></div>
  <div class="book" style="left:968px"><div class="cover" role="img" aria-label="Book cover: Life in the Garden" style="background:linear-gradient(180deg,#3a3a3a 0 70%,#e0392b 70%)"></div><div class="book-title">The Forest</div><div class="book-author">Owen Hale</div></div>
  <div class="btn" style="left:431px;top:488px;width:340px;height:58px">DISCOVER MORE BOOKS</div>
</section>

<section class="about">
  <div class="portrait" role="img" aria-label="Portrait photo of the author"></div>
  <h2 class="section-title" style="left:560px;width:540px;top:1278px">ABOUT TALIA BROOK</h2>
  <div class="rule" style="left:719px;top:1353px"></div>
  <p class="about-copy" style="top:1378px">Lorem ipsum dolor sit amet, consetetur sadipscing elitr, sed diam nonumy eirmod tempor invidunt ut labore dolore magna aliquyam erat, sed diam voluptua. At vero eos et accusam et justo duo dolores et ea rebum. Stet clita kasd gubergren, no sea takimata sanctus est Lorem ipsum dolor sit amet. Lorem ipsum dolor sit amet, consetetur sadipscing elitr, sed diam nonumy eirmod tempor invidunt ut labore et dolore magna aliquyam erat, sed diam voluptua.</p>
  <p class="about-copy" style="top:1512px">Lorem ipsum dolor sit amet, consetetur sadipscing elitr, sed diam nonumy eirmod tempor invidunt ut labore dolore magna aliquyam erat, sed diam voluptua. At vero eos et accusam et justo duo dolores et ea rebum. Stet clita kasd gubergren, no sea takimata sanctus est Lorem ipsum dolor sit amet. Lorem ipsum dolor sit amet, consetetur sadipscing elitr, sed diam nonumy eirmod tempor invidunt ut labore et dolore magna aliquyam erat, sed diam voluptua.</p>
  <div class="btn" style="left:593px;top:1669px;width:220px;height:60px">READ MORE</div>
  <div class="btn" style="left:857px;top:1669px;width:220px;height:60px">CONTACT ME</div>
</section>

<section class="video" role="img" aria-label="Dimmed flat-lay photo of a desk with laptop, camera and gadgets"></section>
<svg class="play" width="108" height="108" viewBox="0 0 108 108"><circle cx="54" cy="54" r="52" fill="#fff" stroke="#222" stroke-width="3"/><path d="M40 30 L80 54 L40 78 Z" fill="#2d1270"/></svg>
<div class="video-caption">WATCH THE FOREST BOOK TRAILER</div>
<div class="btn" style="left:450px;top:2148px;width:296px;height:59px">WATCH MORE VIDEOS</div>

<section class="blog">
  <h2 class="section-title" style="left:0;width:1200px;top:2270px">BLOG</h2>
  <div class="rule" style="left:490px;top:2347px"></div>
  <article class="post" style="left:78px"><div class="post-image" role="img" aria-label="Photo of a woman reading a book"></div><div class="post-body"><h3 class="post-title">Lorem Ipsum</h3><p class="post-text">Lorem ipsum dolor sit amet, consetetur sadipscing elitred diam nonumy eirmod tempor invidunt ut labore dolore magna aliquyam erat sed diam voluptua.</p></div></article>
  <article class="post" style="left:444px"><div class="post-image" role="img" aria-label="Photo of a woman reading a book"></div><div class="post-body"><h3 class="post-title">Lorem Ipsum</h3><p class="post-text">Lorem ipsum dolor sit amet, consetetur sadipscing elitred diam nonumy eirmod tempor invidunt ut labore dolore magna aliquyam erat sed diam voluptua.</p></div></article>
  <article class="post" style="left:806px"><div class="post-image" role="img" aria-label="Photo of a woman reading a book"></div><div class="post-body"><h3 class="post-title">Lorem Ipsum</h3><p class="post-text">Lorem ipsum dolor sit amet, consetetur sadipscing elitred diam nonumy eirmod tempor invidunt ut labore dolore magna aliquyam erat sed diam voluptua.</p></div></article>
</section>

<footer class="footer">
  <div class="copyright">© Talia Brook 2017. All Right Reserved.</div>
  <div class="footer-social">
    <div class="social"><span class="disc" style="background:var(--social-a)"></span>friendloop</div>
    <div class="social"><span class="disc" style="background:var(--social-b)"></span>chirpwave</div>
    <div class="social"><span class="disc" style="background:var(--social-c)"></span>snapmosaic</div>
    <div class="social"><span class="disc" style="background:var(--social-d)"></span>clipvana</div>
  </div>
</footer>

</body>
</html>
```